Small business updating business cards

We have already updated our logo via Pixel Forum and downloaded it (hopefully) for you to use. Now an updated set of business cards for Neil Pollard and Stuart Pollard are also needed... we are also hoping that a copy of our outdated business card designs have uploaded successfully as Microsoft Publisher files. Our Strength Through Unity motto has died a slow death so we are hoping to remove it (and other superfluous lingo if the graphic covers the idea) and instead opt for a fancy graphic (?) on the second side of the card that really reflects our desire to obtain product / haulage from Road Transport / Yard Operators and convert legs of their haulage to rail freight where profitable (bulk haulage / containterised etc). Can you help us look larger, bolder and more robust than we really are (two man show)?
Target Market(s)
Transport Industry
Industry/Entity Type
Business
Contact Information for Business Card
Card details for both N Pollard and S Pollard have been uploaded on the publisher files
Colors
Designer to choose colors to be used in the design.
Requirements
Must have
- Similar theme both sides of card
Should not have
- Black on one side white on the other

```html
<!DOCTYPE html>
<html lang="en">
<head>
<meta charset="utf-8">
<title>Kestrail – Business Card</title>
<link rel="stylesheet" href="https://fonts.googleapis.com/css2?family=Montserrat:ital,wght@0,400;0,700;1,400;1,700;1,800&display=swap">
<style>
  :root {
    --teal: #2586a2;
    --teal-deep: #1f7f9b;
    --gold: #c9a214;
    --olive: #6e8d4a;
    --ink: #3d3d40;
    --rule: #cfcfd2;
    --paper-light: #fbfbfc;
    --paper-shade: #e9e9eb;
    --white: #ffffff;
  }
  html, body {
    margin: 0;
    padding: 0;
    overflow: hidden;
    background: var(--white);
  }
  .card {
    position: relative;
    width: 1200px;
    height: 741px;
    overflow: hidden;
    font-family: "Montserrat", Arial, sans-serif;
    background:
      radial-gradient(ellipse at 30% 40%, var(--paper-light) 0%, transparent 60%),
      linear-gradient(135deg, var(--paper-shade) 0%, var(--paper-light) 35%, #f1f1f3 65%, var(--paper-shade) 100%);
  }
  .brand {
    position: absolute;
    left: 100px;
    top: 278px;
    width: 420px;
    margin: 0;
    font-weight: 700;
    font-size: 78px;
    letter-spacing: -1px;
    line-height: 1;
    color: var(--teal);
  }
  .divider {
    position: absolute;
    left: 599px;
    top: 135px;
    width: 2px;
    height: 365px;
    background: linear-gradient(to bottom, transparent, var(--rule) 15%, var(--rule) 85%, transparent);
  }
  .person {
    position: absolute;
    right: 131px;
    top: 155px;
    text-align: right;
  }
  .person-name {
    margin: 0;
    display: flex;
    align-items: center;
    justify-content: flex-end;
    gap: 10px;
    font-weight: 800;
    font-style: italic;
    font-size: 35px;
    color: var(--teal);
    line-height: 1.1;
  }
  .person-role {
    margin: 10px 0 0;
    font-style: italic;
    font-weight: 400;
    font-size: 28px;
    letter-spacing: 2px;
    color: var(--ink);
  }
  .contact {
    position: absolute;
    left: 678px;
    margin: 0;
    padding: 0;
    list-style: none;
    font-size: 26px;
    letter-spacing: 1.5px;
    color: var(--ink);
  }
  .contact li {
    display: flex;
    align-items: flex-start;
    line-height: 38px;
  }
  .contact .icon {
    width: 20px;
    margin-right: 16px;
    flex: none;
    padding-top: 9px;
  }
  .address { top: 293px; }
  .email { top: 412px; }
  .bottom-arc {
    position: absolute;
    left: 0;
    bottom: 0;
  }
  .phone {
    position: absolute;
    left: 665px;
    top: 648px;
    display: flex;
    align-items: center;
    gap: 18px;
    font-weight: 800;
    font-style: italic;
    font-size: 42px;
    letter-spacing: 5px;
    color: var(--white);
  }
</style>
</head>
<body>
<main class="card">
  <h1 class="brand">Kestrail</h1>

  <div class="divider"></div>

  <section class="person">
    <h2 class="person-name">
      <svg class="name-stripes" width="78" height="28" viewBox="0 0 78 28" aria-hidden="true">
        <defs>
          <linearGradient id="stripeFill" x1="0" y1="1" x2="0" y2="0">
            <stop offset="0" stop-color="var(--gold)"/>
            <stop offset="1" stop-color="var(--teal)"/>
          </linearGradient>
        </defs>
        <g fill="url(#stripeFill)">
          <polygon points="0,28 10,0 17,0 7,28"/>
          <polygon points="19,28 29,0 36,0 26,28"/>
          <polygon points="38,28 48,0 55,0 45,28"/>
          <polygon points="57,28 67,0 74,0 64,28"/>
        </g>
      </svg>
      Stuart Pollard
    </h2>
    <p class="person-role">Director</p>
  </section>

  <ul class="contact address">
    <li>
      <svg class="icon" width="14" height="22" viewBox="0 0 14 22" aria-hidden="true">
        <path d="M7 1a6 6 0 0 0-6 6c0 4.5 6 12 6 12s6-7.5 6-12a6 6 0 0 0-6-6z" fill="none" stroke="var(--gold)" stroke-width="2.4"/>
        <circle cx="7" cy="7" r="2" fill="var(--gold)"/>
      </svg>
      <span>14 Carrow Street<br>Tarrin NSW 2865</span>
    </li>
  </ul>

  <ul class="contact email">
    <li>
      <svg class="icon" width="18" height="13" viewBox="0 0 18 13" aria-hidden="true">
        <rect width="18" height="13" fill="var(--gold)"/>
        <path d="M0 0 9 7 18 0" fill="none" stroke="var(--white)" stroke-width="1.5"/>
      </svg>
      <span>kestrail@mailbox.com</span>
    </li>
    <li>
      <svg class="icon" width="18" height="13" viewBox="0 0 18 13" aria-hidden="true">
        <rect width="18" height="13" fill="var(--gold)"/>
        <path d="M0 0 9 7 18 0" fill="none" stroke="var(--white)" stroke-width="1.5"/>
      </svg>
      <span>kestrail@postnet.com</span>
    </li>
  </ul>

  <svg class="bottom-arc" width="1200" height="741" viewBox="0 0 1200 741" aria-hidden="true">
    <defs>
      <linearGradient id="bandFill" x1="0" y1="0" x2="1" y2="0">
        <stop offset="0.05" stop-color="var(--gold)"/>
        <stop offset="0.55" stop-color="var(--olive)"/>
        <stop offset="1" stop-color="var(--teal-deep)"/>
      </linearGradient>
      <linearGradient id="shadeFill" x1="0" y1="0" x2="0" y2="1">
        <stop offset="0" stop-color="#d8d8db" stop-opacity="0"/>
        <stop offset="1" stop-color="#c9c9cd" stop-opacity="0.6"/>
      </linearGradient>
    </defs>
    <path d="M60 741 C 300 598, 700 548, 1000 572 C 1100 582, 1170 600, 1200 610 L1200 741Z" fill="url(#shadeFill)"/>
    <path d="M80 741 C 310 610, 700 560, 1000 585 C 1100 595, 1170 612, 1200 622 L1200 741Z" fill="url(#bandFill)"/>
    <path d="M205 741 C 420 625, 780 560, 1200 648 L1200 741Z" fill="var(--teal)"/>
  </svg>

  <p class="phone">
    <svg width="46" height="34" viewBox="0 0 46 34" aria-hidden="true">
      <path d="M4 12 C 8 3, 38 3, 42 12 L 36 16 L 31 11 L 15 11 L 10 16 Z" fill="#3a3a3c"/>
      <path d="M10 16 L 14 13 L 32 13 L 36 16 L 40 31 L 6 31 Z" fill="#4a4a4d"/>
      <circle cx="23" cy="23" r="6" fill="#d9d9db"/>
      <circle cx="23" cy="23" r="2" fill="#4a4a4d"/>
    </svg>
    0400 555 019
  </p>
</main>
</body>
</html>
```